Business Card Revision

Need to redesign my business cards for a new professional look. We are a courier company. You can go to www.qvrunners.com to see what we do. The trucks have an old company name (Sprout) on them but that is the company we are just now
changing the name.

Target Market(s)

Potential clients. We service the automotive, plumbing, printing, air freight industries as well as many others.

Industry/Entity Type

Business

Contact Information for Business Card

QVmotion
20864 Lark Fenmore Parkway
Cincinnati, Oh 45873

Thomas R. Wendall
President

tom@qvrunners.com

Main: (513) 555-0147

```html
<!DOCTYPE html>
<html lang="en">
<head>
<meta charset="utf-8">
<title>QV Runners – Business Card</title>
<link rel="stylesheet" href="https://fonts.googleapis.com/css2?family=Open+Sans:wght@400;600;700&display=swap">
<style>
  :root {
    --backdrop: #e4e2de;
    --card: #ffffff;
    --card-shade: #ececec;
    --band: #141414;
    --band-edge: #2c2c2c;
    --ink: #2a2a2a;
    --ink-soft: #555555;
    --on-band: #ffffff;
    --on-band-soft: #d6d6d6;
  }
  * { margin: 0; padding: 0; box-sizing: border-box; }
  html, body {
    width: 1200px;
    height: 1023px;
    overflow: hidden;
    background: var(--backdrop);
    font-family: "Open Sans", Arial, sans-serif;
  }
  .business-card {
    position: absolute;
    left: 180px;
    top: 271px;
    width: 840px;
    height: 480px;
    background: linear-gradient(135deg, var(--card) 0%, var(--card) 55%, var(--card-shade) 100%);
    box-shadow: 0 14px 34px rgba(0,0,0,0.18);
    overflow: hidden;
  }
  .name-band {
    position: absolute;
    left: 0;
    top: 0;
    width: 840px;
    height: 480px;
  }
  .holder-name {
    position: absolute;
    right: 118px;
    top: 66px;
    font-size: 38px;
    font-weight: 400;
    letter-spacing: 1px;
    color: var(--on-band);
  }
  .holder-title {
    position: absolute;
    right: 40px;
    top: 118px;
    font-size: 17px;
    font-weight: 400;
    letter-spacing: 1.5px;
    color: var(--on-band-soft);
  }
  .brand-name {
    position: absolute;
    left: 46px;
    top: 214px;
    display: flex;
    align-items: center;
    gap: 14px;
    font-size: 40px;
    font-weight: 700;
    letter-spacing: 3px;
    color: var(--band);
  }
  .brand-dot {
    width: 22px;
    height: 22px;
    background: var(--band);
  }
  .contact-block {
    position: absolute;
    right: 40px;
    top: 198px;
    text-align: right;
    color: var(--ink-soft);
    font-size: 21px;
    line-height: 34px;
  }
  .contact-block .tag {
    display: inline-block;
    width: 20px;
    margin-left: 8px;
    text-align: left;
    color: var(--ink);
    font-weight: 600;
  }
  .contact-block .division {
    color: var(--ink);
    font-weight: 700;
  }
  .contact-block .address { margin-top: 22px; }
</style>
</head>
<body>
  <article class="business-card">
    <svg class="name-band" viewBox="0 0 840 480" aria-hidden="true">
      <polygon points="300,48 840,48 840,160 300,160 250,104" fill="var(--band)"/>
      <line x1="300" y1="160" x2="840" y2="160" stroke="var(--band-edge)" stroke-width="2"/>
    </svg>
    <div class="holder-name">Thomas R. Wendall</div>
    <div class="holder-title">PRESIDENT</div>

    <div class="brand-name"><span class="brand-dot"></span>QV RUNNERS</div>

    <div class="contact-block">
      <div>(513) 555-0147<span class="tag">P</span></div>
      <div>tom@qvrunners.com<span class="tag">E</span></div>
      <div class="address">
        <div class="division">QVmotion</div>
        <div>20864 Lark Fenmore Parkway</div>
        <div>Cincinnati, Oh 45873</div>
      </div>
    </div>
  </article>
</body>
</html>
```